Tallowind Power - Company Brochure / Display Folder / DL Flyer

We are a trader in environmental commodities based in Australia and require the following 4 designs for an upcoming exhibition;
1) Brochure Folder
Essentially this will be a presentation folder for a number of A4 sheets and will allow us to present business cards. We would like it based on the same design as our stand background - please see attached (001) for reference.
I have attached a file (002) that is basically what i am after, if you could recreate this or something similar it be sufficient. Please change the blue lines to green and incorporate an image that represents solar / environment / renewable energy etc.
Please include our logo (003) as well as the words 'experts in environmental commodity trading'
The back of the folder should have our address, contact number, homepage etc - please refer to the website for these details www.tallowindpower.com.au.
The template is included also, please ensure the deisgn fits within these boundaries for printing (004 / Forme 8)
2) A4 Flyer
We are after a re design of an old flyer that highlights what we do as a business. I have included the wording for this (005) but am open to interpretations as to designs. Please keep it relevant to the graphics requested for the presentation folder.
This will be a single page A4 sheet - very easy.
3) DL Brochure
We will be running a promotion at the exhibition for cash rewards and need a double sided DL flyer designed so the can be handed out. The back of the flyer should have our logo as well as the green graphics consistent with the stand design / background while the front needs to highlight the following promotional offer;
Tallowind Power Cash Rewards Offer
Get more out of your STC's -trade with us to receive instant cash back!
Trade 1000 STC - receive $250 cash rewards card
Trade 5000 STC - receive $500 cash rewards card
(x1 card on the first 1000 + x2 more cards on the first 5000)
Cash rewards cards are valid everywhere that accepts tapcard - cash can even be withdrawn at ATMS!
Offer valid until October 31st 2014
Unregistered Trade Only.
Please keep this text to the left and incorporate an image or graphic on the right side. One that is professional, ties in with the notion of environmental trading but highlights the offer.
Again we open to interpretations with this one.
4) Card Design
Very basic - a design is needed for the rewards card mentioned in the promotion above. I have attached the template / outline required for this (006/ 007) and basically need out logo and a bit of colour on the cash card.
We are open to some ideas but the main thing is being consistent with the stand design that we will be exhibiting in. We like the graphics used and the plain white with the green curved concept. Please ensure the greens from our logo also.
I will do my best to answer any queries you may have, the files should have all the info needed to get started and we usually have a few design amendments after the first drafts are sent through.
Apologies about the timeframe with this one - we are looking to move fast so the earlier submissions will be considered as I can work back and forth with them.
Good Luck
Tallowind Power.

```html
<!DOCTYPE html>
<html lang="en">
<head>
<meta charset="utf-8">
<title>Tallowind Power – Exhibition Stationery</title>
<link rel="stylesheet" href="https://fonts.googleapis.com/css2?family=Arimo:wght@400;700&family=Archivo+Black&display=swap">
<style>
:root{
  --paper:#ffffff;
  --cream:#fdfbdc;
  --cream-deep:#f4f6ae;
  --green:#3fae2a;
  --green-dark:#2a8a1f;
  --lime:#b9e21a;
  --ink:#1d1d1d;
  --rule:#777;
  --band:#dfdfd6;
  --stripe:#111;
}
*{box-sizing:border-box;margin:0;padding:0}
html,body{width:1200px;height:1000px;overflow:hidden;background:var(--paper)}
body{font-family:"Arimo",Arial,sans-serif;color:var(--ink)}
.board{position:relative;width:1200px;height:1000px}
.piece{position:absolute;background:linear-gradient(180deg,var(--cream) 0%,var(--cream-deep) 100%);border:1px solid var(--rule);overflow:hidden}
.swoosh{position:absolute;left:0;right:0;bottom:0;background:radial-gradient(ellipse at 40% 70%,var(--lime) 0%,#d8ef6a 35%,rgba(244,246,174,0) 75%),linear-gradient(180deg,rgba(185,226,26,0) 0%,rgba(120,200,40,.55) 100%)}
.brand{position:absolute;display:flex;flex-direction:column;align-items:flex-start}
.brand-row{display:flex;align-items:center;gap:4px}
.brand-mark{width:1em;height:1em;background:var(--green)}
.brand-name{font-weight:700;color:var(--green);white-space:nowrap;line-height:1}
.brand-tag{color:var(--green-dark);font-style:normal;font-weight:700;white-space:nowrap;margin-top:2px}
.label{position:absolute;font-size:8px;letter-spacing:.5px;color:var(--ink)}
.offer-kicker{color:var(--green);font-weight:700;line-height:1}
.offer-title{font-family:"Archivo Black","Arimo",sans-serif;color:var(--lime);line-height:1;text-shadow:none}
.offer-badge{display:inline-block;border:1px dashed var(--green);color:var(--green);font-weight:700;transform:rotate(-8deg)}
.offer-head{font-weight:700;line-height:1.1}
.offer-tiers{line-height:1.35}
.offer-tiers b{font-weight:700}
.note{line-height:1.4}
.accent{color:var(--green);font-weight:700}
.card-face{position:absolute;border-radius:8px;border:1px solid #aaa;overflow:hidden;background:linear-gradient(180deg,var(--cream) 0%,var(--cream-deep) 100%)}
.card-back{position:absolute;border-radius:8px;border:1px solid #aaa;overflow:hidden;background:var(--paper);text-align:center}
.card-name,.card-number,.card-expiry{position:absolute;font-weight:700;letter-spacing:.18em;white-space:nowrap}
.stripe{position:absolute;left:0;right:0;background:var(--stripe)}
.card-fine{position:absolute;left:8%;right:8%;line-height:1.35;color:#333}
.flyer-copy{position:absolute;left:16px;right:16px;top:62px;font-size:4.6px;line-height:1.45}
.flyer-copy p{margin-bottom:5px}
.grey-band{position:absolute;left:138px;top:535px;width:939px;height:353px;background:var(--band)}
</style>
</head>
<body>
<main class="board">

  <!-- 1) Presentation folder, flat forme -->
  <section class="folder">
    <svg style="position:absolute;left:130px;top:119px" width="520" height="410" viewBox="0 0 520 410" aria-hidden="true">
      <path d="M78 75 L20 75 Q8 75 8 90 L8 185 Q8 198 20 198 L78 198 M78 198 L20 198 Q8 198 8 212 L8 285 Q8 298 20 298 L78 298" fill="none" stroke="#777" stroke-width="1"/>
      <path d="M30 92 l12 10 M30 160 l12 -10 M30 215 l12 10 M30 270 l12 -10" stroke="#999" stroke-dasharray="2 2"/>
      <path d="M78 301 L78 330 Q78 352 100 370 L148 404 L300 345 L310 301" fill="var(--cream)" stroke="#777"/>
    </svg>
    <div class="swoosh" role="img" aria-label="Green flowing curve graphic on pocket flap" style="position:absolute;left:212px;top:430px;width:220px;height:80px;left:212px;right:auto;bottom:auto"></div>

    <div class="piece" style="left:208px;top:119px;width:434px;height:301px">
      <div style="position:absolute;left:216px;top:0;bottom:0;border-left:1px solid #bbb"></div>
      <div class="brand" style="left:318px;top:22px;font-size:13px">
        <div class="brand-row"><span class="brand-mark"></span><span class="brand-name">Tallowind Power</span></div>
        <span class="brand-tag" style="font-size:5px">'experts in environmental commodity trading'</span>
      </div>
      <div class="swoosh" role="img" aria-label="Green and lime flowing curve graphic across the folder" style="height:150px"></div>
    </div>
    <span class="label" style="left:608px;top:424px">1) FOLDER</span>
  </section>

  <!-- 3) DL brochure -->
  <section class="dl-brochure">
    <div class="piece" style="left:655px;top:119px;width:100px;height:201px;padding:10px 8px">
      <div class="offer-kicker" style="font-size:7px">Tallowind Power</div>
      <div class="offer-title" style="font-size:11px">Cash Rewards</div>
      <span class="offer-badge" style="font-size:7px;padding:1px 3px;margin-left:48px">Offer</span>
      <p class="offer-head" style="font-size:6px;margin-top:6px">Get more out of your STC's -trade with us to receive instant cash back</p>
      <p class="offer-tiers" style="font-size:3.6px;margin-top:4px"><b>Trade 1000 STC</b> – receive $250 cash rewards card<br><b>Trade 5000 STC</b> – receive $500 cash rewards card</p>
      <p class="offer-tiers" style="font-size:3.6px;margin-top:3px">x1 card on the first 1000<br>+ x2 more cards on the first 5000</p>
      <div class="swoosh" role="img" aria-label="Green curve graphic with tilted rewards card" style="height:90px"></div>
    </div>
    <div class="piece" style="left:764px;top:119px;width:96px;height:201px;padding:18px 8px">
      <p class="note" style="font-size:5px">Cash rewards cards are valid everywhere that accepts</p>
      <p class="accent" style="font-size:8px">tapcard - cash</p>
      <p class="note" style="font-size:5px">can even be withdrawn at ATMS!</p>
      <p class="note" style="font-size:5px;margin-top:8px">Offer valid until October 31st 2014<br>Unregistered Trade Only.</p>
      <div class="swoosh" role="img" aria-label="Green curve graphic" style="height:70px"></div>
      <div class="brand" style="left:10px;top:162px;font-size:7px">
        <div class="brand-row"><span class="brand-mark"></span><span class="brand-name">Tallowind Power</span></div>
        <span class="brand-tag" style="font-size:3px">Address here</span>
      </div>
    </div>
    <span class="label" style="left:735px;top:324px">3) DL BROCHURE</span>
  </section>

  <!-- 4) Rewards card -->
  <section class="rewards-card">
    <div class="card-face" style="left:658px;top:339px;width:119px;height:75px">
      <div class="brand" style="left:52px;top:6px;font-size:6px">
        <div class="brand-row"><span class="brand-mark"></span><span class="brand-name">Tallowind Power</span></div>
      </div>
      <span class="card-name" style="left:14px;top:30px;font-size:5px">NAME HERE</span>
      <span class="card-number" style="left:14px;top:38px;font-size:6px">0123456789</span>
      <span class="card-expiry" style="left:14px;top:47px;font-size:5px">EXPIRE: 1/1/2015</span>
      <div class="swoosh" role="img" aria-label="Green curve graphic" style="height:28px"></div>
    </div>
    <div class="card-back" style="left:658px;top:422px;width:122px;height:78px">
      <p class="card-fine" style="top:4px;font-size:2.6px">Solution provided by Rewards Made Easy, a member of the Northgate Direct Group.</p>
      <div class="stripe" style="top:12px;height:10px"></div>
      <p class="card-fine" style="top:26px;font-size:2.6px">Congratulations on receiving your Gift Card!<br>Use your card wherever tapcard is accepted. Activate before use on 1800 555 347. Keep your card safe at all times. Card Number: XXXX XXXX XXXX XXXX</p>
    </div>
    <span class="label" style="left:668px;top:504px">4) CARD</span>
  </section>

  <!-- 2) A4 flyer -->
  <section class="a4-flyer">
    <div class="piece" style="left:875px;top:119px;width:202px;height:286px;background:var(--cream)">
      <div class="brand" style="left:70px;top:14px;font-size:9px">
        <div class="brand-row"><span class="brand-mark"></span><span class="brand-name">Tallowind Power</span></div>
        <span class="brand-tag" style="font-size:3.5px">'experts in environmental commodity trading'</span>
      </div>
      <div class="flyer-copy">
        <p>Tallowind Power<br>(including SwiftPay graphic)</p>
        <p>Trade with confidence, take advantage of the highest market prices and make the most of industry leading settlement times. Best Price Guarantee – we won't be beaten. Our traders work tirelessly to stay on top of the STC and LGC markets, allowing the best pricing for all our customers, with no minimum trade and no brokerage or admin fees. Standard, 72 hour settlements – 3 day turnaround.</p>
        <p>We appreciate the importance of cash flow to a business and never miss payments. With 3 settlements every week you are certain to receive funds within 72 hours of submission. Ask about SwiftPay – the fastest settlements available.</p>
        <p>Our Account Managers have good experience in dealing with the complexities of forms and jobs, in particular large commercial submissions. We work closely with the Renewable Certificates Authority to make sure approvals come through fast and accurately. Pricing, settlement, platform and service – we have it all. Tallowind Power is one of the largest independent STC traders in Australia.</p>
        <p>To learn more about trading with Tallowind Power visit www.tallowindpower.com.au or call 1300 555 218<br>Tallowind Power – We pay higher, faster.</p>
      </div>
    </div>
    <span class="label" style="left:1010px;top:409px">2) A4 FLYER</span>
  </section>

  <!-- Enlarged flat views -->
  <section class="grey-band">
    <div class="piece" style="left:92px;top:28px;width:210px;height:300px;border-color:#ccc">
      <div class="brand" style="left:70px;top:30px;font-size:13px">
        <div class="brand-row"><span class="brand-mark"></span><span class="brand-name">Tallowind Power</span></div>
        <span class="brand-tag" style="font-size:5px">'experts in environmental commodity trading'</span>
      </div>
      <div class="swoosh" role="img" aria-label="Green and lime flowing curve graphic on folder cover" style="height:170px"></div>
    </div>

    <div class="piece" style="left:342px;top:28px;width:118px;height:301px;border-color:#ccc;padding:18px 10px">
      <div class="offer-kicker" style="font-size:9px">Tallowind Power</div>
      <div class="offer-title" style="font-size:15px">Cash Rewards</div>
      <span class="offer-badge" style="font-size:10px;padding:1px 4px;margin-left:58px">Offer</span>
      <p class="offer-head" style="font-size:8.5px;margin-top:10px">Get more out of your STC's -trade with us to receive instant cash back</p>
      <p class="offer-tiers" style="font-size:5px;margin-top:6px"><b>Trade 1000 STC</b> – receive $250 cash rewards card<br><b>Trade 5000 STC</b> – receive $500 cash rewards card</p>
      <p class="offer-tiers" style="font-size:5px;margin-top:4px">x1 card on the first 1000<br>+ x2 more cards on the first 5000</p>
      <div class="swoosh" role="img" aria-label="Green curve graphic with tilted rewards card" style="height:130px"></div>
    </div>

    <div class="piece" style="left:486px;top:28px;width:98px;height:301px;background:var(--paper);border-color:#ccc;padding:34px 8px">
      <p class="note" style="font-size:6.5px">Cash rewards cards are valid everywhere that accepts</p>
      <p class="accent" style="font-size:10px">tapcard - cash</p>
      <p class="note" style="font-size:6.5px">can even be withdrawn at ATMS!</p>
      <p class="note" style="font-size:6.5px;margin-top:14px">Offer valid until October 31st 2014<br>Unregistered Trade Only.</p>
      <div class="swoosh" role="img" aria-label="Green curve graphic" style="height:95px"></div>
      <div class="brand" style="left:10px;top:248px;font-size:8px">
        <div class="brand-row"><span class="brand-mark"></span><span class="brand-name">Tallowind Power</span></div>
        <span class="brand-tag" style="font-size:3.5px">'experts in environmental commodity trading'</span>
        <span class="brand-tag" style="font-size:4px;color:var(--ink);font-weight:400">Address here</span>
      </div>
    </div>

    <div class="card-face" style="left:669px;top:59px;width:203px;height:128px">
      <div class="brand" style="left:86px;top:12px;font-size:10px">
        <div class="brand-row"><span class="brand-mark"></span><span class="brand-name">Tallowind Power</span></div>
        <span class="brand-tag" style="font-size:4px">'experts in environmental commodity trading'</span>
      </div>
      <span class="card-name" style="left:28px;top:56px;font-size:9px">NAME HERE</span>
      <span class="card-number" style="left:28px;top:70px;font-size:11px">0123456789</span>
      <span class="card-expiry" style="left:28px;top:88px;font-size:9px">EXPIRE: 1/1/2015</span>
      <div class="swoosh" role="img" aria-label="Green curve graphic" style="height:48px"></div>
    </div>

    <div class="card-back" style="left:669px;top:203px;width:203px;height:128px">
      <p class="card-fine" style="top:8px;font-size:4px;font-style:italic">Solution provided by Rewards Made Easy, a member of the Northgate Direct Group.</p>
      <div class="stripe" style="top:18px;height:22px"></div>
      <p class="card-fine" style="top:46px;font-size:4px">Congratulations on receiving your Gift Card!</p>
      <p class="card-fine" style="top:56px;font-size:3.4px">Your gift card can be used to purchase goods and services in retailers accepting tapcard throughout Australia. You must activate your card before use. To activate your card and for all cardholder enquiries, please call 1800 555 347 during business hours. To check your balance visit www.rewardsmadeeasy.com.au.<br>Your card cannot be used to withdraw cash at retail outlets. Damaged or altered cards will be cancelled. Keep your PIN private at all times.</p>
      <p class="card-fine" style="top:106px;font-size:3.6px">Card Number: XXXX XXXX XXXX XXXX<br>Card Pin: XXXX &nbsp; Expiry: DD MMMMMMMM YYYY</p>
    </div>
  </section>

</main>
</body>
</html>
```